Jolly Paws Business Card Update

I have a business card which I love. I want to keep the same logo, colours, font and style. I want to upgrade the scripting and remove some elements and add others.
On the front side under Services - remove the existing wording and insert - Providing individual coaching strategies to create happy, healthy and social canine companions
Under Rebecca Thornbury amend the current wording to read: Qualified in Dog Behavioural Training, Natural Animal Healthcare and Animal Health Science
On the reverse side to remove the web address.

```html
<!DOCTYPE html>
<html lang="en">
<head>
<meta charset="utf-8">
<title>Jolly Paws – Business Card</title>
<link rel="stylesheet" href="https://fonts.googleapis.com/css2?family=Arimo:wght@400;700&display=swap">
<style>
  :root {
    --bg: #2b2b2d;
    --blue-light: #0a9fdc;
    --blue-deep: #1c3c9c;
    --red-bright: #e31e26;
    --red-dark: #7a0f14;
    --red-ring: #a3141b;
    --cream: #efe8cf;
    --white: #ffffff;
    --ink-dark: #2a1a10;
  }
  * { box-sizing: border-box; margin: 0; padding: 0; }
  html, body {
    width: 1200px; height: 900px; overflow: hidden;
    background: var(--bg);
    font-family: "Arimo", Arial, sans-serif;
  }
  .canvas { position: relative; width: 1200px; height: 900px; }

  .card {
    position: absolute;
    width: 640px; height: 366px;
    overflow: hidden;
    box-shadow: 0 14px 30px rgba(0,0,0,.55);
  }

  /* Front */
  .card--front {
    left: 70px; top: 50px;
    background: linear-gradient(160deg, var(--blue-light) 0%, #0a6fc4 45%, var(--blue-deep) 100%);
  }
  .card__swoosh { position: absolute; left: 0; top: 0; width: 100%; height: 100%; }
  .brand {
    position: absolute; left: 0; right: 0; top: 44px;
    display: flex; flex-direction: column; align-items: center;
    color: var(--white);
  }
  .brand__mark {
    width: 110px; height: 110px; border-radius: 50%;
    background: var(--cream);
    border: 9px solid var(--red-ring);
  }
  .brand__name {
    margin-top: 14px;
    font-size: 40px; font-weight: 700; letter-spacing: 2px;
    text-transform: uppercase; color: var(--cream);
  }
  .brand__tagline {
    margin-top: 6px;
    font-size: 17px; letter-spacing: 1.5px; text-transform: uppercase;
  }

  /* Back */
  .card--back {
    left: 490px; top: 484px;
    background: linear-gradient(160deg, var(--blue-light) 0%, #0a86cf 50%, #0f5fb8 100%);
  }
  .back__mark {
    position: absolute; left: 92px; top: 46px;
    width: 126px; height: 126px; border-radius: 50%;
    background: var(--cream);
    border: 10px solid var(--red-ring);
  }
  .back__rule {
    position: absolute; width: 1px; background: rgba(255,255,255,.8);
  }
  .back__rule--services { left: 262px; top: 36px; height: 150px; }
  .services {
    position: absolute; left: 290px; top: 40px; width: 300px;
    color: var(--white);
  }
  .services__title { font-size: 21px; font-weight: 400; letter-spacing: .5px; margin-bottom: 8px; }
  .services__text { font-size: 17px; line-height: 1.25; padding-left: 18px; }

  .band {
    position: absolute; left: 0; right: 0; top: 205px; height: 26px;
    background: var(--cream);
    color: var(--ink-dark);
    font-size: 15px; line-height: 26px; text-align: center;
  }
  .back__lower {
    position: absolute; left: 0; right: 0; top: 231px; bottom: 0;
    background: radial-gradient(ellipse at 42% 70%, var(--red-bright) 0%, #b5161c 45%, var(--red-dark) 100%);
    color: var(--white);
  }
  .person {
    position: absolute; left: 24px; top: 16px; width: 320px; text-align: center;
  }
  .person__name { font-size: 20px; font-weight: 700; letter-spacing: .5px; text-transform: uppercase; }
  .person__quals { font-size: 15px; line-height: 1.2; margin-top: 3px; }
  .back__rule--contact { left: 362px; top: 16px; height: 100px; }
  .contact {
    position: absolute; left: 380px; right: 16px; top: 28px;
    list-style: none; font-size: 17px; white-space: nowrap;
  }
  .contact__item { display: flex; align-items: center; gap: 9px; margin-bottom: 12px; }
  .contact__icon { width: 20px; height: 20px; flex: none; }
</style>
</head>
<body>
<main class="canvas">

  <section class="card card--front" aria-label="Business card front">
    <svg class="card__swoosh" viewBox="0 0 640 366" preserveAspectRatio="none" aria-hidden="true">
      <defs>
        <linearGradient id="swooshRed" x1="0" y1="0" x2="1" y2="0">
          <stop offset="0" stop-color="#7a0f14"/>
          <stop offset="0.55" stop-color="#e31e26"/>
          <stop offset="1" stop-color="#7a0f14"/>
        </linearGradient>
      </defs>
      <path d="M0 300 Q330 235 640 240 L640 366 L0 366 Z" fill="url(#swooshRed)"/>
      <path d="M0 300 Q330 235 640 240" fill="none" stroke="#efe8cf" stroke-width="4"/>
    </svg>
    <div class="brand">
      <div class="brand__mark"></div>
      <h1 class="brand__name">Jolly Paws</h1>
      <p class="brand__tagline">Happy Dogs, Happy Owners</p>
    </div>
  </section>

  <section class="card card--back" aria-label="Business card back">
    <div class="back__mark"></div>
    <span class="back__rule back__rule--services"></span>
    <div class="services">
      <h2 class="services__title">SERVICES</h2>
      <p class="services__text">Providing individual coaching strategies to create happy, healthy and social canine companions</p>
    </div>

    <p class="band">Promoting communication and connection between dogs and their families</p>

    <div class="back__lower">
      <div class="person">
        <p class="person__name">Rebecca Thornbury</p>
        <p class="person__quals">Qualified in Dog Behavioural Training,<br>Natural Animal Healthcare<br>and Animal Health Science</p>
      </div>
      <span class="back__rule back__rule--contact"></span>
      <ul class="contact">
        <li class="contact__item">
          <svg class="contact__icon" viewBox="0 0 20 20" aria-hidden="true">
            <circle cx="10" cy="10" r="9.5" fill="#fff"/>
            <rect x="7" y="4.5" width="6" height="11" rx="1" fill="#b5161c"/>
            <rect x="8" y="6" width="4" height="6" fill="#fff"/>
          </svg>
          <span>0412 736 205</span>
        </li>
        <li class="contact__item">
          <svg class="contact__icon" viewBox="0 0 20 20" aria-hidden="true">
            <circle cx="10" cy="10" r="9.5" fill="#fff"/>
            <rect x="5" y="6.5" width="10" height="7" fill="#b5161c"/>
            <path d="M5 6.5 L10 11 L15 6.5" fill="none" stroke="#fff" stroke-width="1.2"/>
          </svg>
          <span>hello@jollypaws.com</span>
        </li>
      </ul>
    </div>
  </section>

</main>
</body>
</html>
```